Marrowgate Auctions Business Cards Design Needed

I need a business card design that is modern looking - double sided (maybe just my logo on the back, but open to suggestions) - the overall design is up to you. I want it to be easy to read - not over the top flashy. I already have a company logo which I uploaded so that needs to be used. The colors of my logo are the colors I want on the card... so blue and gray (do need to match the logo colors).

Requirements
Must have
• Would like the card to be sleek, modern and easy to ready

```html
<!DOCTYPE html>
<html lang="en">
<head>
<meta charset="utf-8">
<title>Marrowgate Auctions Business Cards</title>
<link rel="stylesheet" href="https://fonts.googleapis.com/css2?family=Montserrat:wght@400;700&display=swap">
<style>
  :root {
    --backdrop: #1d1d1f;
    --card: #ffffff;
    --brand-blue: #1e7bc4;
    --brand-gray: #4a4a4d;
    --text-gray: #58585b;
    --rule: #5a5a5d;
  }
  * { margin: 0; padding: 0; box-sizing: border-box; }
  html, body {
    width: 1200px; height: 960px; overflow: hidden;
    background: var(--backdrop);
    font-family: "Montserrat", sans-serif;
  }
  .stage {
    position: relative; width: 1200px; height: 960px;
    display: flex; flex-direction: column; align-items: center; justify-content: center; gap: 60px;
  }
  .card {
    position: relative; width: 700px; height: 400px;
    background: var(--card);
  }
  .wordmark {
    display: flex; align-items: center; gap: 14px;
    font-weight: 700; color: var(--brand-blue); letter-spacing: 0.02em;
    text-transform: uppercase;
  }
  .wordmark-square { width: 22px; height: 22px; background: var(--brand-blue); flex: none; }
  .card-front .wordmark {
    position: absolute; left: 0; right: 0; top: 0; bottom: 0;
    justify-content: center; font-size: 38px;
  }
  .card-back .wordmark {
    position: absolute; right: 40px; top: 70px; font-size: 28px;
  }
  .card-back .wordmark-square { width: 18px; height: 18px; }
  .rule-long {
    position: absolute; left: 330px; right: 40px; top: 140px;
    height: 2px; background: var(--rule);
  }
  .tagline {
    position: absolute; right: 40px; top: 166px; text-align: right;
    font-size: 16px; line-height: 1.3; color: var(--text-gray);
  }
  .holder { position: absolute; left: 40px; top: 200px; width: 290px; }
  .holder-name { font-size: 30px; font-weight: 700; color: var(--brand-blue); line-height: 1.1; }
  .holder-title { font-size: 15px; color: var(--text-gray); margin-top: 4px; }
  .holder-rule { height: 2px; background: var(--rule); margin-top: 10px; }
  .contacts { position: absolute; left: 40px; top: 290px; list-style: none; }
  .contacts li {
    display: flex; align-items: center; gap: 12px;
    font-size: 17px; color: var(--text-gray); line-height: 30px;
  }
  .contacts svg { width: 18px; height: 18px; fill: var(--brand-blue); flex: none; }
</style>
</head>
<body>
<main class="stage">
  <section class="card card-front" aria-label="Card front">
    <div class="wordmark"><span class="wordmark-square"></span>Marrowgate Auctions</div>
  </section>

  <section class="card card-back" aria-label="Card back">
    <div class="wordmark"><span class="wordmark-square"></span>Marrowgate Auctions</div>
    <div class="rule-long"></div>
    <p class="tagline">Improving Charity<br>Auctions Nationwide</p>

    <div class="holder">
      <h1 class="holder-name">Reed Calloway</h1>
      <p class="holder-title">Owner / President - Auctioneer</p>
      <div class="holder-rule"></div>
    </div>

    <ul class="contacts">
      <li>
        <svg viewBox="0 0 24 24" aria-hidden="true"><path d="M6.6 10.8a15 15 0 0 0 6.6 6.6l2.2-2.2a1 1 0 0 1 1-.25 11.4 11.4 0 0 0 3.6.57 1 1 0 0 1 1 1V20a1 1 0 0 1-1 1A17 17 0 0 1 3 4a1 1 0 0 1 1-1h3.5a1 1 0 0 1 1 1c0 1.25.2 2.45.57 3.57a1 1 0 0 1-.25 1z"/></svg>
        702-555-0186
      </li>
      <li>
        <svg viewBox="0 0 24 24" aria-hidden="true"><path d="M2 5h20v14H2z M4 7v.4l8 5.2 8-5.2V7z" fill-rule="evenodd"/></svg>
        marrowgateauctions@mail.com
      </li>
      <li>
        <svg viewBox="0 0 24 24" aria-hidden="true"><path d="M12 2a10 10 0 1 0 0 20 10 10 0 0 0 0-20zm0 2.2a7.8 7.8 0 0 1 0 15.6 7.8 7.8 0 0 1 0-15.6zM12 7l4 3-1.5 5h-5L8 10z"/></svg>
        bidrevival.com
      </li>
    </ul>
  </section>
</main>
</body>
</html>
```